Weight loss surgery restaurant card

We need to create a card for patients who have undergone weight loss surgery to take to restaurants so they can request smaller meals. These patients have had surgery on their stomach so that they can only consume half to one cup of food at a time. So normal sized restaurant meals are way too big (and cost a lot). This card they can present to the restaurant to communicate the fact that they have had weight loss surgery and therefore request a smaller meal portion at reduced cost

Target Market(s)

Restaurants serving weight loss surgery patients

Industry/Entity Type

Health Care

Contact Information for Business Card

This will be a plastic card similar to business card size.

Requirements
Must have
• The front of the card should include the following text:
• The individual bearing this card has undergone weight loss surgery.
• This surgery restricts portion sizes to between half and one cup of food at a time.
• Please give consideration to allowing smaller portions of your regular meals to be ordered to reduce wastage and excess costs.
• Example: a half size portion priced at two thirds of usual cost.
• The back of the card will have spaces for the person to write certain information. These are the categories that can be filled in by hand:
• Name:
• Procedure performed:
• Date of procedure (month/year):
• Treating Clinic Name:
• Treating Clinic Signature:
• Somewhere down the bottom should be something along the lines of:
• supplied from bernardwhitlow.com.au
Nice to have
• A nice design with imagery/colours etc ... not just the text on a white background! Bright attractive colours preferred.
• I have uploaded my logo ... a roughly triangular image followed by my name etc. The triangular logo image could be used somewhere on the card and this logo can be interchangeable for other clinics who purchase the card.
• **Please note that I don't want my name to be included as part of the logo on the card ... just use the triangular image on the side of the logo without the following name**
• Also, the colouring of the card does not have to reflect my logo colours as I am anticipating interchanging this logo with other logos if other clinics choose to adopt the card. I am interested to see other, more generic, colour choices as well as my logo colours

```html
<!DOCTYPE html>
<html lang="en">
<head>
<meta charset="utf-8">
<title>Weight Loss Surgery Restaurant Card</title>
<link rel="stylesheet" href="https://fonts.googleapis.com/css2?family=Questrial&display=swap">
<style>
  :root {
    --page-bg: #16171c;
    --card-deep: #16184a;
    --card-mid: #262a7e;
    --accent-teal: #4fd6c6;
    --text-soft: #a4a8cc;
    --field-bg: #eef1f4;
    --field-text: #9fb3c0;
    --field-line: #7fd9cf;
  }
  * { box-sizing: border-box; margin: 0; padding: 0; }
  html, body {
    width: 1200px;
    height: 900px;
    overflow: hidden;
    background: var(--page-bg);
    font-family: "Questrial", "Century Gothic", sans-serif;
  }
  .sheet {
    width: 1200px;
    height: 900px;
    display: flex;
    flex-direction: column;
    align-items: center;
    justify-content: center;
    gap: 36px;
  }
  .card {
    position: relative;
    width: 680px;
    height: 388px;
    border-radius: 6px;
    overflow: hidden;
    background: radial-gradient(ellipse at 62% 48%, var(--card-mid) 0%, var(--card-deep) 78%);
    box-shadow: 0 14px 40px rgba(0, 0, 0, 0.55);
  }
  .dot-wave {
    position: absolute;
    right: 0;
    bottom: 0;
    width: 360px;
    height: 300px;
    background:
      radial-gradient(ellipse at 78% 72%, rgba(79, 214, 198, 0.42) 0%, rgba(79, 214, 198, 0.12) 38%, rgba(79, 214, 198, 0) 68%);
  }
  .dot-wave--front {
    width: 320px;
    height: 340px;
    background:
      radial-gradient(ellipse at 86% 64%, rgba(79, 214, 198, 0.4) 0%, rgba(79, 214, 198, 0.1) 40%, rgba(79, 214, 198, 0) 70%);
  }

  /* Front */
  .card-front { padding: 34px 40px; }
  .front-copy { position: relative; width: 470px; }
  .lead {
    color: var(--accent-teal);
    font-size: 22px;
    line-height: 1.12;
    font-weight: 700;
  }
  .note {
    color: var(--text-soft);
    font-size: 16px;
    line-height: 1.2;
    margin: 6px 0 12px;
  }
  .front-copy .lead + .note { margin-top: 6px; }

  /* Back */
  .card-back { padding: 30px 36px; }
  .clinic-mark {
    position: relative;
    display: flex;
    align-items: center;
    gap: 12px;
  }
  .clinic-dot {
    width: 38px;
    height: 38px;
    border-radius: 50%;
    background: var(--accent-teal);
  }
  .clinic-name {
    color: var(--accent-teal);
    font-size: 30px;
    letter-spacing: 0.5px;
    line-height: 1;
  }
  .clinic-role {
    color: var(--accent-teal);
    font-size: 10px;
    letter-spacing: 1.2px;
    text-transform: uppercase;
    margin-top: 4px;
  }
  .record-box {
    position: relative;
    margin-top: 18px;
    width: 420px;
    padding: 14px 20px 12px;
    border-radius: 12px;
    background: var(--field-bg);
  }
  .record-field {
    display: flex;
    align-items: flex-end;
    gap: 6px;
    color: var(--field-text);
    font-size: 14px;
    height: 28px;
  }
  .record-field span.line {
    flex: 1;
    border-bottom: 1px solid var(--field-line);
    margin-bottom: 4px;
  }
  .supplier {
    position: relative;
    margin-top: 22px;
    padding-left: 30px;
  }
  .supplier-label {
    color: var(--text-soft);
    font-size: 15px;
  }
  .supplier-url {
    color: var(--accent-teal);
    font-size: 17px;
    margin-top: 2px;
  }
</style>
</head>
<body>
<main class="sheet">

  <section class="card card-back" aria-label="Card back">
    <div class="dot-wave" role="img" aria-label="Flowing teal dotted wave pattern"></div>
    <div class="clinic-mark">
      <div class="clinic-dot"></div>
      <div>
        <div class="clinic-name">Bernard Whitlow</div>
        <div class="clinic-role">General, Upper GI &amp; Bariatric Surgeon</div>
      </div>
    </div>
    <div class="record-box">
      <div class="record-field">Name:<span class="line"></span></div>
      <div class="record-field">Procedure performed:<span class="line"></span></div>
      <div class="record-field">Date of procedure (month/year):<span class="line"></span></div>
      <div class="record-field">Treating Clinic Name:<span class="line"></span></div>
      <div class="record-field">Treating Clinic Signature:<span class="line"></span></div>
    </div>
    <div class="supplier">
      <p class="supplier-label">Purchased through</p>
      <p class="supplier-url">www.bernardwhitlow.com.au</p>
    </div>
  </section>

  <section class="card card-front" aria-label="Card front">
    <div class="dot-wave dot-wave--front" role="img" aria-label="Flowing teal dotted wave pattern"></div>
    <div class="front-copy">
      <p class="lead">The individual bearing this card<br>has undergone weight loss surgery.</p>
      <p class="note">Around 500,000 of these procedures are<br>performed around the world every year.</p>
      <p class="lead">This surgery restricts portion<br>sizes to between half and<br>one cup of food at a time.</p>
      <p class="note">Please give consideration to allowing<br>smaller portions of your regular<br>meals to be ordered to reduce<br>wastage and excess costs.</p>
      <p class="lead">Example: a half size portion priced<br>at two thirds of usual cost.</p>
    </div>
  </section>

</main>
</body>
</html>
```